We require a business card that promotes our Electrical business. Things we would like included are;
1) our business name, Bright Path Electrical and Communication
2) Our Electrical licence, EC 73620
3) Our ABN, 41 297 506 183
4) Our website, www.korvanelectric.com.au
5) Our Email, info@korvanelectric.com.au
6) Our contact number, 0462 158 704
7) Our address, 57 Larkfield Rd West Dunmore Perth 6109
8) Our logo, I will attach this (can you please change it so the ackground is white not black)
9) Our colours are red and white and perhaps some black
10) Managing Director Tomasz Relhuvan
11) the back to say 'notes' and have some lines for writing

Target Market(s)

General

Industry/Entity Type

Electrical

Contact Information for Business Card

Include the colour white, black and red.

Font styles to use
Sans Serif

Requirements
Nice to have
• A thunder bolt or a power point or a cord or something electrical, cartoon image of a cartoon like electrical tradie

```html
<!DOCTYPE html>
<html lang="en">
<head>
<meta charset="utf-8">
<title>Bright Path Electrical and Communication – Business Card</title>
<link href="https://fonts.googleapis.com/css2?family=Questrial&display=swap" rel="stylesheet">
<style>
  :root {
    --brand-red: #e0202a;
    --ink: #1a1a1a;
    --ink-soft: #555555;
    --card: #ffffff;
    --backdrop: #d6d6d6;
  }
  * { margin: 0; padding: 0; box-sizing: border-box; }
  html, body {
    width: 1200px;
    height: 777px;
    overflow: hidden;
    background: var(--backdrop);
    font-family: "Questrial", Arial, sans-serif;
  }
  .canvas { position: relative; width: 1200px; height: 777px; }

  .card {
    position: absolute;
    top: 269px;
    width: 441px;
    height: 246px;
    background: var(--card);
  }
  .card--front { left: 96px; }
  .card--back  { left: 639px; }

  /* Brand mark: name set in the text face with one plain circle beside it */
  .brand {
    position: absolute;
    display: flex;
    align-items: center;
    gap: 9px;
    color: var(--brand-red);
    white-space: nowrap;
    transform: translateX(-50%);
  }
  .brand__dot {
    border-radius: 50%;
    background: var(--brand-red);
    flex: none;
  }

  .card--front .brand { left: 50%; top: 82px; font-size: 24px; }
  .card--front .brand__dot { width: 40px; height: 40px; }

  .tagline {
    position: absolute;
    left: 0;
    right: 0;
    top: 147px;
    text-align: center;
    color: var(--brand-red);
    font-size: 11.5px;
    letter-spacing: 0.3px;
  }

  .card--back .brand { left: 121px; top: 56px; font-size: 14px; gap: 7px; flex-direction: column; }
  .card--back .brand__dot { width: 30px; height: 30px; }

  .person { position: absolute; left: 223px; top: 52px; }
  .person__name { color: var(--brand-red); font-size: 11px; line-height: 13px; }
  .person__role { color: var(--ink); font-size: 8px; line-height: 11px; }
  .person__rule { width: 9px; height: 1px; background: var(--ink); margin-top: 5px; }

  .contact {
    position: absolute;
    left: 223px;
    top: 119px;
    list-style: none;
    color: var(--ink-soft);
    font-size: 8px;
    line-height: 11.6px;
  }
  .website {
    position: absolute;
    left: 223px;
    top: 198px;
    color: var(--ink-soft);
    font-size: 8px;
    letter-spacing: 0.2px;
  }
</style>
</head>
<body>
<main class="canvas">
  <section class="card card--front" aria-label="Card front">
    <div class="brand"><span class="brand__dot"></span>Bright Path</div>
    <p class="tagline">Electrical and Communication</p>
  </section>

  <section class="card card--back" aria-label="Card back">
    <div class="brand"><span class="brand__dot"></span>Bright Path</div>

    <div class="person">
      <p class="person__name">Tomasz Relhuvan</p>
      <p class="person__role">Managing Director</p>
      <div class="person__rule"></div>
    </div>

    <ul class="contact">
      <li>Phone: 0462 158 704</li>
      <li>Electrical License. EC 73620</li>
      <li>ABN. 41 297 506 183</li>
      <li>info@korvanelectric.com.au</li>
      <li>57 Larkfield Rd West</li>
      <li>Dunmore Perth 6109</li>
    </ul>

    <p class="website">www.korvanelectric.com.au</p>
  </section>
</main>
</body>
</html>
```